VARNEK Consulting Services “Coming Soon” Landing Page

MORE INTO IN Design Brief for Web Designer document attached

1. Project Overview
Client: VARNEK Consulting Services
Project: Build a static, responsive “Coming Soon” landing page (HTML/CSS/JS)
Timeline: Target launch date in June 7, 2025
Point of Contact: Martin Holloway (Managing Director)
 • Email: martin@varnekconsulting.com
 • Phone: 555-304-7728
Background:
VARNEK Consulting Services is a boutique IT consultancy specializing in enterprise cloud solutions, microservices, FlowMesh migrations, and AGENTIC AI-driven integrations. We are launching a new website to capture CIO-level leads, build brand awareness, and communicate our key value propositions before the full site goes live. This “Coming Soon” page should reflect our brand identity, target CIO and enterprise IT leaders, and collect email addresses for early access to whitepapers, case studies, and consultations.

2. Goals & Objectives
1. Brand Reinforcement
• Convey a contemporary, corporate, and professional look that aligns with VARNEK’s positioning as a specialized, agile, high-ROI consultancy.
• Utilize our brand colors (green, red, blue, gold) and typography (Segoe UI) consistently.
2. Lead Generation
• Implement a simple email-capture form (“Notify Me”) that submits to mailto:info@varnekconsulting.com.
• Convey clear messaging so visitors understand why they should sign up (exclusive early insights, whitepapers, invitations to consult).
3. Enterprise Leadership-Focused Messaging
• Immediately communicate our core value proposition (“Enterprise Modernization Reimagined”) and differentiation versus larger consulting firms.
• Introduce AGENTIC AI use cases to demonstrate cutting-edge capabilities.
4. Responsive & Accessible
• Build a mobile-first responsive design using a 12-column grid.
• Follow best practices for HTML5 markup, CSS3, and lightweight JS (for countdown timer).
5. SEO & Technical Must-Haves
• Include basic SEO metadata and Open Graph tags.
• Provide a favicon placeholder.
• Placeholder for a Privacy Policy link in the footer.
Updates

Designs look the same

Industry/Entity Type

VARNEK Consulting Services is a boutique IT consultancy specializing in enterprise cloud solutions, microservices, FlowMesh migrations, and AGENTIC AI-driven integrations.

Coding

Coded - Design and coding required

Number of Pages Required

1 page

Requirements
Must have
• Below are our primary brand colors with hex codes (derived from CMYK values in the uploaded “Color and Font.jpg”): • Green (Globe Icon): #3BFF05 • Red (Q-Shape Icon): #EF1C03 • Blue (Circle Icon): #456EFF • Gold (Connector Icon): #F7C217 • Dark Gray / Text Color: #1A1A1A Use these colors for text highlights, buttons, icons, and accents. The overall page background is white or very light gray (#F9F9F9) to keep the design clean.
Should not have
• Colors outside the scheme provided

```html
<!DOCTYPE html>
<html lang="en">
<head>
<meta charset="utf-8">
<title>VARNEK Consulting Services – Enterprise Modernization Reimagined</title>
<link href="https://fonts.googleapis.com/css2?family=Open+Sans:wght@400;600;700;800&display=swap" rel="stylesheet">
<style>
:root{
  --blue:#456EFF;
  --blue-deep:#3a56c9;
  --gold:#F7C217;
  --red:#EF1C03;
  --green:#3BFF05;
  --dark:#1A1A1A;
  --light:#F9F9F9;
  --white:#ffffff;
}
*{box-sizing:border-box;margin:0;padding:0}
html,body{width:1200px;height:3648px;overflow:hidden;background:var(--light)}
body{font-family:"Open Sans",Arial,sans-serif;color:var(--dark);position:relative}

/* hero */
.hero{position:absolute;left:0;top:0;width:1200px;height:1330px}
.hero-photo{position:absolute;left:0;top:0;width:1200px;height:1060px;
  background:linear-gradient(120deg,#e9ecf3 0%,#c9cfdc 45%,#f2f2f2 100%)}
.nav-band{position:absolute;left:0;top:0}
.main-nav{position:absolute;left:80px;top:82px;display:flex;gap:64px}
.main-nav a{color:var(--gold);font-weight:700;font-size:30px;text-decoration:none;letter-spacing:.5px}
.brand{position:absolute;right:36px;top:20px;display:flex;align-items:center;gap:14px;
  background:var(--white);padding:14px 22px;border-radius:8px}
.brand-dot{width:52px;height:52px;border-radius:50%;background:var(--blue)}
.brand-name{font-weight:700;color:var(--blue-deep);font-size:28px;line-height:1.05}
.hero-title-box{position:absolute;left:735px;top:290px}
.hero-title{position:absolute;left:755px;top:338px;width:430px;text-align:center;color:var(--white);
  font-weight:800;font-size:45px;line-height:1.12}
.hero-wave{position:absolute;left:0;top:860px}
.hero-copy{position:absolute;left:90px;top:960px;width:1020px;text-align:center}
.hero-lead{color:var(--gold);font-weight:800;font-size:27px;line-height:1.3;text-transform:uppercase}
.hero-text{color:var(--white);font-size:21px;line-height:1.5;margin-top:30px}

/* intro */
.intro{position:absolute;left:110px;top:1340px;width:980px;text-align:center;font-size:20px;line-height:1.5}

/* features */
.features{position:absolute;left:0;top:1540px;width:1200px;height:860px}
.feature-photo{position:absolute;left:370px;top:40px;width:500px;height:820px;
  background:radial-gradient(ellipse at 50% 40%,#f4d9b5 0%,#9fb5e6 55%,#e9eef9 100%);border-radius:10px 10px 0 0}
.feature{position:absolute;width:330px}
.feature h3{color:var(--blue-deep);font-weight:800;font-size:33px;line-height:1.08;text-transform:uppercase}
.feature p{font-size:19px;line-height:1.35;margin-top:8px}
.feature-top{left:400px;top:10px;width:400px;text-align:center;z-index:2}
.feature-top h3{background:var(--light);padding-bottom:4px}
.feature-top p{background:var(--light)}
.f-left{left:30px;text-align:center}
.f-right{right:30px;text-align:center}

/* comparison */
.compare{position:absolute;left:0;top:2400px;width:1200px;height:420px;background:var(--blue-deep)}
.compare-lead{color:var(--gold);font-weight:800;font-size:27px;text-align:center;margin-top:28px;line-height:1.25;text-transform:uppercase}
.compare-title{color:var(--white);font-weight:800;font-size:38px;text-align:center;margin-top:18px}
.compare-cards{display:flex;justify-content:center;gap:50px;margin-top:30px}
.compare-card{width:300px;height:210px;border:4px solid var(--white);border-radius:10px;position:relative;
  padding:26px 18px 10px;text-align:center;color:var(--white);font-size:13px;font-weight:600;line-height:1.3;text-transform:uppercase}
.compare-card .tag{display:inline-block;background:var(--blue);color:var(--white);font-weight:800;font-size:18px;padding:2px 18px;margin-bottom:6px;border-radius:3px}

/* cta */
.cta{position:absolute;left:0;top:2820px;width:1200px;height:500px;background:var(--dark);text-align:center}
.cta h2{color:var(--gold);font-weight:800;font-size:40px;margin-top:70px}
.cta p{color:var(--white);font-size:24px;line-height:1.45;width:800px;margin:24px auto 0}
.cta-actions{display:flex;justify-content:center;gap:80px;margin-top:50px}
.btn{background:var(--gold);color:var(--blue-deep);font-weight:800;font-size:26px;padding:12px 40px;text-decoration:none}

/* footer */
.site-footer{position:absolute;left:0;top:3320px;width:1200px;height:328px;background:var(--white)}
.contact-line{position:absolute;left:60px;display:flex;align-items:center;gap:14px;font-size:22px}
.contact-line a{color:var(--dark);text-decoration:none}
.icon-box{width:34px;height:34px;background:var(--dark);border-radius:4px}
.legal{position:absolute;right:40px;bottom:26px;font-size:14px;color:var(--dark)}
</style>
</head>
<body>

<header class="hero">
  <div class="hero-photo" role="img" aria-label="Photo of two smiling business professionals working together at a laptop in a bright office"></div>
  <svg class="nav-band" width="1200" height="220" viewBox="0 0 1200 220">
    <path d="M0 0H860C800 80 700 170 520 170C360 170 200 130 0 200Z" fill="var(--blue-deep)"/>
  </svg>
  <nav class="main-nav">
    <a href="#">HOME</a><a href="#">ABOUT</a><a href="#">SERVICES</a><a href="#contact">CONTACT</a>
  </nav>
  <div class="brand"><span class="brand-dot"></span><span class="brand-name">VARNEK<br>Consulting Services</span></div>
  <svg class="hero-title-box" width="465" height="300" viewBox="0 0 465 300">
    <path d="M60 0H465V300H40C0 230 0 70 60 0Z" fill="var(--blue-deep)" opacity=".92"/>
  </svg>
  <h1 class="hero-title">ENTERPRISE MODERNIZATION REIMAGINED</h1>
  <svg class="hero-wave" width="1200" height="470" viewBox="0 0 1200 470">
    <path d="M0 60C300 0 600 140 900 80C1040 50 1130 20 1200 40V470H0Z" fill="var(--blue)"/>
    <path d="M0 110C320 40 620 170 920 110C1050 85 1140 70 1200 80V470H0Z" fill="var(--blue-deep)"/>
    <path d="M0 420C300 470 900 390 1200 450V470H0Z" fill="var(--light)"/>
  </svg>
  <div class="hero-copy">
    <p class="hero-lead">Retire legacy systems and transition to secure, cloud-native infrastructure designed for scalability, AI integration, and future-ready performance.</p>
    <p class="hero-text">Today's leaders don't have time for templated strategies and slow-moving firms. At VARNEK, we deliver tailored solutions that align with your business objectives, accelerate outcomes, and scale as you grow. Our senior experts work directly with your team to deliver fast, measurable impact—no layers, no delays. From modernizing legacy platforms to enabling intelligent automation, we solve the complex integration challenges others overlook so you can focus on leading the future!</p>
  </div>
</header>

<p class="intro">Imagine a partner that doesn't hand you a recycled playbook but builds a smarter path forward that's all about your goals. At VARNEK Consulting Services, we don't do cookie-cutter. We roll up our sleeves, work alongside your team, and deliver fast, measurable results that move the needle. While others push templates, we unlock possibilities—modern systems, real efficiency, and AI that actually works. No fluff. No junior handoffs. Just bold execution that gets you ahead and keeps you there.</p>

<section class="features">
  <div class="feature-photo" role="img" aria-label="Photo of an enthusiastic consultant in a hat and glasses pointing upward with both hands"></div>
  <div class="feature feature-top"><h3>Senior Access, Always</h3><p>Speak directly to the experts. No junior filters. No delays.</p></div>
  <div class="feature f-left" style="top:190px"><h3>Speed That Scales</h3><p>Rapid execution means you see value faster—and scale without friction.</p></div>
  <div class="feature f-right" style="top:190px"><h3>Custom Paths to Modernization</h3><p>Your transformation, built to fit and built to last.</p></div>
  <div class="feature f-left" style="top:400px"><h3>Elite Expertise, Zero Fluff</h3><p>Our DNA is Nimbus, FlowMesh, and bleeding-edge AI.</p></div>
  <div class="feature f-right" style="top:400px"><h3>Smarter Spend</h3><p>High impact. Low overhead. We outperform the big firms without their price tags.</p></div>
</section>

<section class="compare">
  <p class="compare-lead">Smart IT and business leaders are moving fast—here's why<br>they're choosing agile over traditional consulting</p>
  <h2 class="compare-title">RESPONSIVE TABLE</h2>
  <div class="compare-cards">
    <div class="compare-card"><span class="tag">ASPECT</span><br>Approach<br>Turnaround time<br>Cost efficiency<br>Expert accessibility<br>Scalability focus<br>Innovation &amp; AI</div>
    <div class="compare-card"><span class="tag">ASPECT</span><br>Tailored agile execution<br>Accelerated<br>Transparent pricing<br>Direct access to specialists<br>Hyper-focused on your enterprise needs<br>Embedded agentic AI &amp; adaptive architectures</div>
    <div class="compare-card"><span class="tag">ASPECT</span><br>Standardized, rigid frameworks<br>Average to extended timelines<br>Premium costs &amp; overhead<br>Layers of account managers<br>Generic, one-size-fits-all solutions<br>Legacy automation, limited adaptability</div>
  </div>
</section>

<section class="cta" id="contact">
  <h2>SCHEDULE A CONSULTATION</h2>
  <p>Legacy isn't a roadmap. It's a roadblock. Let's architect what's next—secure, scalable, AI-enabled, and aligned with your business goals. (Let's Reimagine Your Enterprise Together)</p>
  <div class="cta-actions">
    <a class="btn" href="mailto:info@varnekconsulting.com">CONTACT US</a>
    <a class="btn" href="mailto:info@varnekconsulting.com">BOOK A STRATEGY SESSION</a>
  </div>
</section>

<footer class="site-footer">
  <div class="contact-line" style="top:70px">
    <svg width="34" height="34" viewBox="0 0 34 34"><rect x="2" y="7" width="30" height="20" rx="2" fill="none" stroke="var(--dark)" stroke-width="2.5"/><path d="M3 9L17 19L31 9" fill="none" stroke="var(--dark)" stroke-width="2.5"/></svg>
    <a href="mailto:info@varnekconsulting.com">info@varnekconsulting.com</a>
  </div>
  <div class="contact-line" style="top:130px">
    <span class="icon-box"></span>
    <a href="#">https://www.proflink.net/company/varnek</a>
  </div>
  <p class="legal">Privacy Policy &nbsp;|&nbsp; © 2025 VARNEK Consulting Services. All rights reserved</p>
</footer>

</body>
</html>
```